New Business Card Design Project

I need a design for business cards, i am an electrical business called "Tandor Electrical and Communications" i need the cards to be double sided with the company logo on the back (attached) the front needs to say my company name, web site, email address, telephone number, and ABN number and electrical license number. I am open to different arrangements of the information but would like the background to be incorporating something electrical or something that looks smart. open to all additional ideas also.

The company colours are orange and grey see logo attached.

Business Name: Tandor Electrical and Communications
Website: tandorelectricalandcomms.example.au
Email: brent@tandorelectricalandcomms.example.au
Telephone(mobile): 0481203967
ABN: 71829034618
Lic No: 830472F

Target Market(s)

Business entities, Project Managers, Accounts, Clients

Industry/Entity Type

Electrician

Contact Information for Business Card

I need a design for business cards, i am an electrical business called "Tandor Electrical and Communications" i need the cards to be double sided with the company logo on the back (attached) the front needs to say my company name

Font styles to use
Serif
Sans Serif

Colors
f37122
5c5c5c

Requirements
Must have
• Must have the Logo on the back open to different ways of it being on the back but had in mind to keep it central but again open to other options
Nice to have
• A real modern cool background that is eye catching yet contemporary
Should not have
• No backgrounds of a light bulb or plug or anything like that

```html
<!DOCTYPE html>
<html lang="en">
<head>
<meta charset="UTF-8">
<title>Tandor Electrical and Communications – Business Cards</title>
<link rel="stylesheet" href="https://fonts.googleapis.com/css2?family=Questrial&display=swap">
<style>
  :root {
    --stage: #2f2f2f;
    --card: #050505;
    --orange: #f8a81c;
    --white: #ffffff;
    --muted: #e6e6e6;
  }
  * { margin: 0; padding: 0; box-sizing: border-box; }
  html, body {
    width: 1200px;
    height: 900px;
    overflow: hidden;
    background: var(--stage);
    font-family: "Questrial", sans-serif;
  }
  .stage {
    position: relative;
    width: 1200px;
    height: 900px;
  }
  .card {
    position: absolute;
    width: 620px;
    height: 354px;
    background: var(--card);
    border-radius: 22px;
    overflow: hidden;
    box-shadow: 0 18px 40px rgba(0,0,0,0.55);
  }

  /* Back of card */
  .card-back { left: 200px; top: 70px; }
  .card-back .brand {
    position: absolute;
    left: 110px;
    top: 118px;
    width: 420px;
    color: var(--white);
  }
  .brand-name {
    font-size: 58px;
    letter-spacing: 3px;
    line-height: 1;
    text-transform: uppercase;
  }
  .brand-sub {
    margin-top: 10px;
    font-size: 17px;
    letter-spacing: 1.6px;
    text-transform: uppercase;
  }
  .brand-mark {
    display: inline-block;
    width: 14px;
    height: 14px;
    background: var(--orange);
    margin-right: 12px;
    vertical-align: 8px;
  }
  .card-back .site {
    position: absolute;
    left: 40px;
    bottom: 30px;
    font-size: 19px;
    color: var(--white);
  }
  .card-back .site .domain { color: var(--orange); }

  /* Front of card */
  .card-front { left: 380px; top: 476px; }
  .card-front .brand {
    position: absolute;
    right: 34px;
    top: 44px;
    text-align: left;
    color: var(--white);
  }
  .card-front .brand-name { font-size: 38px; letter-spacing: 2px; }
  .card-front .brand-sub { font-size: 11px; margin-top: 6px; letter-spacing: 1.2px; }
  .card-front .brand-mark { width: 10px; height: 10px; margin-right: 8px; vertical-align: 6px; }
  .licence {
    margin-top: 8px;
    font-size: 13px;
    color: var(--white);
  }
  .label { color: var(--orange); }

  .side-tab {
    position: absolute;
    left: 0;
    top: 196px;
    width: 38px;
    height: 158px;
    background: var(--orange);
    border-radius: 0 22px 0 0;
  }
  .contact {
    position: absolute;
    left: 62px;
    top: 196px;
    color: var(--white);
  }
  .person-name {
    font-size: 30px;
    color: var(--orange);
    letter-spacing: 1px;
    text-transform: uppercase;
    line-height: 1;
  }
  .person-role {
    margin-top: 5px;
    font-size: 14px;
    text-transform: uppercase;
  }
  .abn { font-size: 14px; margin-top: 3px; }
  .contact-list {
    list-style: none;
    margin-top: 12px;
    font-size: 15px;
  }
  .contact-list li {
    display: flex;
    align-items: center;
    gap: 10px;
    margin-bottom: 4px;
  }
  .contact-list svg { width: 13px; height: 13px; fill: var(--orange); flex: none; }
</style>
</head>
<body>
<main class="stage">

  <section class="card card-back" aria-label="Card back">
    <div class="brand">
      <div class="brand-name"><span class="brand-mark"></span>Tandor</div>
      <div class="brand-sub">Electrical &amp; Communications</div>
    </div>
    <p class="site">www.<span class="domain">tandorelectricalandcomms</span>.example.au</p>
  </section>

  <section class="card card-front" aria-label="Card front">
    <div class="brand">
      <div class="brand-name"><span class="brand-mark"></span>Tandor</div>
      <div class="brand-sub">Electrical &amp; Communications</div>
      <p class="licence"><span class="label">Lic No:</span> 830472F</p>
    </div>

    <div class="side-tab"></div>

    <div class="contact">
      <h1 class="person-name">Marlo Kendrick</h1>
      <p class="person-role">Director</p>
      <p class="abn"><span class="label">ABN:</span> 71829034618</p>
      <ul class="contact-list">
        <li>
          <svg viewBox="0 0 24 24" aria-hidden="true"><path d="M6.6 10.8a15.1 15.1 0 0 0 6.6 6.6l2.2-2.2a1 1 0 0 1 1-.25 11.4 11.4 0 0 0 3.6.57 1 1 0 0 1 1 1V20a1 1 0 0 1-1 1A17 17 0 0 1 3 4a1 1 0 0 1 1-1h3.5a1 1 0 0 1 1 1c0 1.25.2 2.45.57 3.57a1 1 0 0 1-.25 1z"/></svg>
          0481 203 967
        </li>
        <li>
          <svg viewBox="0 0 24 24" aria-hidden="true"><path d="M2 5h20v14H2z M4 7v.5l8 5 8-5V7l-8 5z" fill-rule="evenodd"/></svg>
          brent@tandorelectricalandcomms.example.au
        </li>
        <li>
          <svg viewBox="0 0 24 24" aria-hidden="true"><path d="M12 2a10 10 0 1 0 0 20 10 10 0 0 0 0-20zm0 2c.9 0 2.1 1.8 2.6 5H9.4C9.9 5.8 11.1 4 12 4zM4.3 11h3a19 19 0 0 0 .1 2h-3a8 8 0 0 1-.1-2zm5 0h5.4a17 17 0 0 1 0 2H9.3a17 17 0 0 1 0-2zm7.4 0h3a8 8 0 0 1 0 2h-3a19 19 0 0 0 0-2zM9.4 15h5.2c-.5 3.2-1.7 5-2.6 5s-2.1-1.8-2.6-5z"/></svg>
          www.tandorelectricalandcomms.example.au
        </li>
      </ul>
    </div>
  </section>

</main>
</body>
</html>
```